Business Card Design

We need a basic, but modern design card. Our business is a local Queanbeyan/Canberra courier service, but can organise interstate delivery if needed. Our fleet ranges from 1 tonne vans to 8 tonne trucks.

Industry/Entity Type

Business

Contact Information for Business Card

Harbourline Freight
14 Tarrant Road
Merrindale NSW 2635

Owen Prescott
CEO

Phone: 02 61847315
Fax: 02 61847398
email: owen@harbourlinefreight.com.au

```html
<!DOCTYPE html>
<html lang="en">
<head>
<meta charset="utf-8">
<title>Harbourline Freight – Business Card</title>
<link rel="stylesheet" href="https://fonts.googleapis.com/css2?family=Questrial&family=Michroma&family=Carlito&display=swap">
<style>
  :root {
    --brand-blue: #00adef;
    --ink-grey: #5f6062;
    --text-dark: #3d3d3d;
    --card-stock: #eeeeee;
    --card-stock-light: #f4f4f4;
    --card-edge: #555555;
    --frame: #444444;
    --page: #ffffff;
  }
  * { box-sizing: border-box; margin: 0; padding: 0; }
  html, body {
    width: 1200px; height: 1000px; overflow: hidden;
    background: var(--page);
  }
  .presentation {
    position: relative;
    width: 1200px; height: 1000px;
    border: 2px solid var(--frame);
    background: var(--page);
  }
  .card {
    position: absolute;
    border: 1px solid var(--card-edge);
    background: linear-gradient(135deg, var(--card-stock-light), var(--card-stock) 60%, var(--card-stock-light));
  }
  .card-front {
    width: 678px; height: 387px;
    left: 112px; top: 106px;
    transform: rotate(-8.5deg);
    display: flex; align-items: center; justify-content: center; gap: 22px;
  }
  .brand-mark {
    width: 46px; height: 46px;
    background: var(--brand-blue);
  }
  .brand-name {
    font-family: "Questrial", sans-serif;
    font-size: 34px;
    letter-spacing: 1px;
    text-transform: uppercase;
    color: var(--brand-blue);
  }
  .card-back {
    width: 707px; height: 405px;
    left: 385px; top: 526px;
    overflow: hidden;
  }
  .edge-block {
    position: absolute;
    left: 0; top: 127px;
    width: 127px; height: 124px;
    background: var(--brand-blue);
  }
  .holder-name {
    position: absolute;
    left: 203px; top: 80px;
    font-family: "Michroma", sans-serif;
    font-weight: 400;
    font-variant: small-caps;
    font-size: 38px;
    line-height: 1;
    color: var(--brand-blue);
    letter-spacing: 1px;
    white-space: nowrap;
  }
  .holder-role {
    position: absolute;
    left: 205px; top: 142px;
    font-family: "Michroma", sans-serif;
    font-weight: 700;
    font-size: 19px;
    line-height: 1;
    color: var(--ink-grey);
    letter-spacing: 2px;
  }
  .contact-list {
    position: absolute;
    left: 205px; top: 208px;
    list-style: none;
  }
  .contact-item {
    display: flex; align-items: center;
    height: 24px;
    font-family: "Carlito", sans-serif;
    font-size: 22px;
    color: var(--text-dark);
    letter-spacing: 0.3px;
    white-space: nowrap;
  }
  .contact-item + .contact-item { margin-top: 19px; }
  .contact-item:nth-child(3) { margin-top: 17px; }
  .contact-icon {
    width: 22px; height: 22px;
    margin-right: 24px;
    flex: none;
    fill: var(--brand-blue);
  }
</style>
</head>
<body>
  <main class="presentation">

    <section class="card card-front" aria-label="Card front">
      <span class="brand-mark"></span>
      <span class="brand-name">Harbourline Freight</span>
    </section>

    <section class="card card-back" aria-label="Card back">
      <div class="edge-block"></div>
      <h1 class="holder-name">Owen Prescott</h1>
      <p class="holder-role">CEO</p>
      <ul class="contact-list">
        <li class="contact-item">
          <svg class="contact-icon" viewBox="0 0 24 24" aria-hidden="true">
            <path d="M6.6 2.5l3 3.2-1.9 2.4c1.2 3 3.2 5.2 6.2 6.7l2.3-1.9 3.3 3-1.6 3.1c-7.4-.5-13.6-7-14-14.6z"/>
          </svg>
          <span>02 61847315</span>
        </li>
        <li class="contact-item">
          <svg class="contact-icon" viewBox="0 0 24 24" aria-hidden="true">
            <path d="M6 2h12v5H6zM3 8h18a1 1 0 0 1 1 1v8h-4v-3H6v3H2V9a1 1 0 0 1 1-1zM7 15h10v7H7zm2 2v1h6v-1zm0 2v1h6v-1z"/>
          </svg>
          <span>02 61847398</span>
        </li>
        <li class="contact-item">
          <svg class="contact-icon" viewBox="0 0 24 24" aria-hidden="true">
            <path d="M2 5h20v14H2zm2 2v.4l8 6 8-6V7zm0 2.9V17h16V9.9l-8 6z"/>
          </svg>
          <span>owen@harbourlinefreight.com.au</span>
        </li>
        <li class="contact-item">
          <svg class="contact-icon" viewBox="0 0 24 24" aria-hidden="true">
            <path d="M12 1a7 7 0 0 1 7 7c0 5.2-7 15-7 15S5 13.2 5 8a7 7 0 0 1 7-7zm0 4.2A2.8 2.8 0 1 0 12 10.8 2.8 2.8 0 0 0 12 5.2z"/>
          </svg>
          <span>14 Tarrant Road Merrindale NSW 2635.</span>
        </li>
      </ul>
    </section>

  </main>
</body>
</html>
```